Brovanix Stationery Design Project

We need a stationery design for our new business Brovanix which deals in advanced cleaning technologies such as Ultrasonic cleaning and high pressure cleaning machinery.

Our colour scheme is as per the included files.

We require business cards, letterheads, a brochure folder and email signatures design
Updates

Apologies for the delay in making a decision on this project. We will be making a final decision during the course of next week

Target Market(s)

Industries ranging from medical, automotive, mining, engineering all requiring specialised cleaning services

Industry/Entity Type

Pressure Cleaning

Requirements
Must have
• Please include our supplied logo and colour scheme. The design needs to be professional but creative.

```html
<!DOCTYPE html>
<html lang="en">
<head>
<meta charset="utf-8">
<title>Brovanix Presentation Folder</title>
<link href="https://fonts.googleapis.com/css2?family=Montserrat:wght@800&family=Open+Sans:wght@400;600;700&display=swap" rel="stylesheet">
<style>
  :root {
    --blue-light: #3b66b0;
    --blue-dark: #22326d;
    --navy: #27397a;
    --grey: #939598;
    --white: #ffffff;
    --mark-tint: #cfd7e8;
    --dash: #b3bddb;
    --divider: #4a4a4a;
  }
  html, body { margin: 0; padding: 0; overflow: hidden; background: var(--white); }
  .folder {
    position: relative;
    width: 1200px;
    height: 800px;
    overflow: hidden;
    font-family: "Open Sans", Arial, sans-serif;
    background: var(--white);
  }
  /* Outer cover */
  .cover {
    position: absolute; left: 0; top: 0;
    width: 600px; height: 800px;
    background: var(--grey);
  }
  .cover__band {
    position: absolute; left: 0; top: 0;
    width: 228px; height: 800px;
    background: linear-gradient(90deg, var(--blue-light), var(--blue-dark));
  }
  .cover__strip {
    position: absolute; left: 34px; top: 0;
    width: 159px; height: 772px;
    background: var(--grey);
  }
  .brand__dot {
    position: absolute; left: 191px; top: 363px;
    width: 74px; height: 74px;
    border-radius: 50%;
    background: var(--navy);
  }
  .brand {
    position: absolute; left: 274px; top: 366px;
    color: var(--white);
  }
  .brand__name {
    font-family: "Montserrat", Arial, sans-serif;
    font-weight: 800;
    font-size: 38px;
    line-height: 1;
    letter-spacing: 0.3px;
    margin: 0 0 6px 0;
    white-space: nowrap;
  }
  .brand__tagline {
    font-size: 16px;
    font-weight: 400;
    line-height: 1.1;
    letter-spacing: -0.2px;
    margin: 0;
    white-space: nowrap;
  }
  .contact {
    position: absolute; left: 51px; top: 632px;
    margin: 0; padding: 0; list-style: none;
    color: var(--white);
    font-size: 9.5px;
    font-weight: 600;
    letter-spacing: 0.5px;
  }
  .contact li { height: 19px; }
  .contact li.contact__address { margin-bottom: 10px; }
  .contact b { font-weight: 700; }
  /* Fold line */
  .fold {
    position: absolute; left: 600px; top: 0;
    width: 2px; height: 800px;
    background: var(--divider);
  }
  /* Inner / back panel */
  .panel-art { position: absolute; left: 602px; top: 0; }
  .watermark {
    position: absolute; left: 737px; top: 345px;
    width: 330px;
    text-align: center;
    font-family: "Montserrat", Arial, sans-serif;
    font-weight: 800;
    font-size: 62px;
    color: var(--mark-tint);
    line-height: 1;
  }
</style>
</head>
<body>
<main class="folder">
  <section class="cover">
    <div class="cover__band"></div>
    <div class="cover__strip"></div>
    <div class="brand__dot"></div>
    <div class="brand">
      <p class="brand__name">BROVANIX</p>
      <p class="brand__tagline">Advanced Cleaning Technologies</p>
    </div>
    <ul class="contact">
      <li class="contact__address"><b>Address:</b> your address here</li>
      <li><b>Phone:</b> 000-000-0000</li>
      <li><b>Fax:</b> 000-000-0000</li>
      <li><b>Website:</b> brovanix.com</li>
      <li><b>Email:</b> info@brovanix.com</li>
    </ul>
  </section>

  <div class="fold"></div>

  <svg class="panel-art" width="598" height="800" viewBox="602 0 598 800" aria-hidden="true">
    <defs>
      <linearGradient id="pocket-fill" x1="0" y1="0" x2="1" y2="0">
        <stop offset="0" stop-color="#3b66b0"/>
        <stop offset="1" stop-color="#22326d"/>
      </linearGradient>
    </defs>
    <polygon class="pocket" points="737,548 1200,548 1200,800 606,800" fill="url(#pocket-fill)"/>
    <line class="slot-cut" x1="964" y1="710" x2="1132" y2="710" stroke="#b3bddb" stroke-width="1.3" stroke-dasharray="10 8"/>
    <line class="slot-cut" x1="951" y1="710" x2="916" y2="782" stroke="#b3bddb" stroke-width="1.3" stroke-dasharray="10 8"/>
  </svg>

  <div class="watermark">BROVANIX</div>
</main>
</body>
</html>
```